Accounting firm needing business card / letterhead designed
Marcus T. Elbering, CPA
marcus@fernquill.com
www.fernquill.com
482 N Harlow Ave Alderwick, OR 43719
419-555-0172

```html
<!DOCTYPE html>
<html lang="en">
<head>
<meta charset="utf-8">
<title>Fernquill — Business Card</title>
<link href="https://fonts.googleapis.com/css2?family=Roboto:wght@400;700&family=Michroma&display=swap" rel="stylesheet">
<style>
  :root {
    --backdrop: #1d1d1f;
    --paper: #f4f4f4;
    --navy: #27235c;
    --navy-deep: #1f1b4e;
    --green: #5ea315;
    --ink: #2b2b2b;
    --rule: #cfcfcf;
    --white: #ffffff;
  }
  * { margin: 0; padding: 0; box-sizing: border-box; }
  html, body {
    width: 1200px; height: 1001px; overflow: hidden;
    background: var(--backdrop);
    font-family: "Roboto", Arial, sans-serif;
  }
  .card {
    position: absolute; left: 306px; width: 589px; height: 330px;
    box-shadow: 0 4px 10px rgba(0,0,0,.45);
    overflow: hidden;
  }
  .card--front { top: 133px; background: var(--paper); }
  .card--back { top: 539px; background: linear-gradient(180deg, var(--navy) 0%, var(--navy-deep) 100%); }

  .brand-name {
    position: absolute;
    font-family: "Michroma", Arial, sans-serif;
    font-weight: 400;
    letter-spacing: 1px;
    white-space: nowrap;
    transform: translate(-50%, -50%);
  }
  .card--front .brand-name { left: 165px; top: 150px; font-size: 29px; color: var(--navy); }
  .card--back .brand-name { left: 294px; top: 160px; font-size: 40px; color: var(--white); }

  .divider {
    position: absolute; left: 290px; top: 103px; width: 1px; height: 128px;
    background: var(--rule);
  }
  .contact { position: absolute; left: 314px; top: 99px; color: var(--ink); }
  .contact__name {
    font-size: 18px; font-weight: 700; color: var(--navy); letter-spacing: -0.2px;
  }
  .contact__name .credential { font-size: 14px; font-weight: 400; color: var(--navy); }
  .contact__list { list-style: none; margin-top: 13px; }
  .contact__item {
    display: flex; align-items: center; height: 18.5px; font-size: 14px;
  }
  .contact__item svg { width: 13px; height: 13px; margin: 0 7px 0 1px; flex: none; }
  .contact__address { margin-top: 9px; font-size: 14px; line-height: 19px; }

  .accent-bands { position: absolute; left: 0; bottom: 0; width: 589px; height: 18px; }

  .card--back .site {
    position: absolute; left: 0; right: 0; top: 274px; text-align: center;
    color: var(--white); font-size: 14px; letter-spacing: .2px;
  }
  .site strong { font-weight: 700; }
</style>
</head>
<body>

<section class="card card--front">
  <div class="brand-name">Fernquill</div>
  <div class="divider"></div>
  <div class="contact">
    <p class="contact__name">MARCUS T. ELBERING<span class="credential">, CPA</span></p>
    <ul class="contact__list">
      <li class="contact__item">
        <svg viewBox="0 0 16 16" aria-hidden="true"><path fill="#5ea315" d="M4.2 1.5l2 3.2-1.3 1.4c.8 1.9 2.3 3.4 4.2 4.3l1.4-1.3 3.2 2-1 2.6C7.6 13.4 2.6 8.4 1.8 2.5z"/></svg>
        555-555-0172
      </li>
      <li class="contact__item">
        <svg viewBox="0 0 16 16" aria-hidden="true"><rect x="1" y="3" width="14" height="10" fill="#5ea315"/><path d="M1.5 3.5L8 9l6.5-5.5" fill="none" stroke="#f4f4f4" stroke-width="1.2"/></svg>
        info@fernquill.com
      </li>
      <li class="contact__item">
        <svg viewBox="0 0 16 16" aria-hidden="true"><g fill="none" stroke="#5ea315" stroke-width="1.2"><circle cx="8" cy="8" r="6.5"/><ellipse cx="8" cy="8" rx="3" ry="6.5"/><path d="M1.5 8h13M2.5 4.8h11M2.5 11.2h11"/></g></svg>
        www.fernquill.com
      </li>
    </ul>
    <p class="contact__address">482 N Harlow Ave<br>Alderwick, OR 43719</p>
  </div>
  <svg class="accent-bands" viewBox="0 0 589 18" aria-hidden="true">
    <polygon points="0,9 283,9 277,18 0,18" fill="#27235c"/>
    <polygon points="294,0 589,0 589,18 282,18" fill="#5ea315"/>
  </svg>
</section>

<section class="card card--back">
  <div class="brand-name">Fernquill</div>
  <p class="site">www.<strong>fernquill</strong>.com</p>
</section>

</body>
</html>
```